Maple Ridge business card design

Card needs to include the following text/items:
Company Logo
Tobin Marsh
Phone # - 555-318-7642
service@mapleridgelandscaping.example
Lawn & landscape maintenance services

```html
<!DOCTYPE html>
<html lang="en">
<head>
<meta charset="utf-8">
<title>Maple Ridge Landscaping – Business Card</title>
<link rel="stylesheet" href="https://fonts.googleapis.com/css2?family=Cinzel:wght@700&family=Montserrat:wght@400;600&family=Lato:wght@400&display=swap">
<style>
  :root {
    --backdrop: #7b6450;
    --card-white: #ffffff;
    --forest: #1f4a2a;
    --forest-deep: #183d22;
    --olive: #8fa83a;
    --olive-light: #9bbf3a;
    --orange: #f5a323;
    --bark: #7a3b22;
  }
  * { margin: 0; padding: 0; box-sizing: border-box; }
  html, body { width: 900px; height: 1200px; overflow: hidden; }
  body { background: var(--backdrop); position: relative; }

  .card {
    position: absolute;
    left: 82px;
    width: 733px;
    height: 429px;
    border-radius: 22px;
    overflow: hidden;
  }
  .card--front { top: 138px; background: var(--card-white); }
  .card--back {
    top: 634px;
    background: radial-gradient(ellipse 520px 420px at 100% 15%, var(--olive) 0%, #55782f 45%, var(--forest) 80%);
  }

  .card__band { position: absolute; inset: 0; }

  .brand-name {
    position: absolute;
    font-family: "Montserrat", sans-serif;
    font-weight: 600;
    font-size: 34px;
    line-height: 1.2;
    text-align: center;
  }
  .card--front .brand-name { left: 30px; width: 320px; top: 120px; color: var(--forest); }
  .card--back .brand-name { left: 0; right: 0; top: 160px; color: var(--card-white); }

  .holder {
    position: absolute;
    right: 40px; top: 60px;
    text-align: right;
    font-family: "Cinzel", serif;
    font-weight: 700;
  }
  .holder__name { font-size: 33px; color: var(--forest); line-height: 1; }
  .holder__role { font-size: 17px; color: var(--bark); margin-top: 8px; letter-spacing: 1px; }

  .contact {
    position: absolute;
    right: 40px; top: 330px;
    font-family: "Montserrat", sans-serif;
    color: var(--card-white);
    list-style: none;
  }
  .contact__item { display: flex; align-items: center; justify-content: flex-end; gap: 10px; height: 31px; }
  .contact__phone { font-size: 22px; letter-spacing: 0.5px; }
  .contact__email { font-size: 16px; }
  .contact__icon { width: 24px; height: 24px; flex: none; }

  .grass {
    position: absolute;
    left: 0; right: 0; bottom: 0;
    height: 95px;
    background: linear-gradient(180deg, rgba(24,61,34,0) 0%, var(--forest-deep) 45%, var(--forest-deep) 100%);
  }
  .tagline {
    position: absolute;
    left: 0; right: 0; top: 397px;
    text-align: center;
    font-family: "Lato", sans-serif;
    font-size: 15px;
    color: var(--olive-light);
  }
</style>
</head>
<body>

<section class="card card--front">
  <svg class="card__band" viewBox="0 0 733 429" aria-hidden="true">
    <path d="M0,360 C200,350 330,300 430,270 C540,240 640,228 733,230 L733,429 L0,429 Z" fill="var(--forest)"/>
    <path d="M440,252 C540,224 640,212 733,212" fill="none" stroke="var(--orange)" stroke-width="6"/>
  </svg>

  <div class="brand-name">Maple Ridge<br>Landscaping</div>

  <div class="holder">
    <div class="holder__name">Tobin Marsh</div>
    <div class="holder__role">OWNER</div>
  </div>

  <ul class="contact">
    <li class="contact__item">
      <span class="contact__phone">555-318-7642</span>
      <svg class="contact__icon" viewBox="0 0 24 24" aria-hidden="true">
        <circle cx="12" cy="12" r="11" fill="var(--bark)" stroke="#e8d9c8" stroke-width="1.5"/>
        <path d="M8.5 7c.6-.5 1.4-.4 1.8.2l.9 1.4c.3.5.2 1.1-.2 1.5l-.6.5c.6 1.3 1.6 2.3 2.9 2.9l.5-.6c.4-.4 1-.5 1.5-.2l1.4.9c.6.4.7 1.2.2 1.8l-.6.6c-.6.6-1.6.8-2.4.4-2.6-1.2-4.6-3.2-5.8-5.8-.4-.8-.2-1.8.4-2.4z" fill="#fff"/>
      </svg>
    </li>
    <li class="contact__item">
      <span class="contact__email">service@mapleridgelandscaping.example</span>
      <svg class="contact__icon" viewBox="0 0 24 24" aria-hidden="true">
        <circle cx="12" cy="12" r="11" fill="var(--bark)" stroke="#e8d9c8" stroke-width="1.5"/>
        <rect x="6.5" y="8" width="11" height="8" fill="#fff"/>
        <path d="M6.5 8 L12 12.5 L17.5 8" fill="none" stroke="var(--bark)" stroke-width="1.2"/>
      </svg>
    </li>
  </ul>
</section>

<section class="card card--back">
  <div class="brand-name">Maple Ridge<br>Landscaping</div>
  <div class="grass" role="img" aria-label="Grass along the bottom edge"></div>
  <p class="tagline">Lawn &amp; landscape maintenance services</p>
</section>

</body>
</html>
```